Lone Willow Estate Vault Reserve Wine Label (Front and Back)

I need to create an elite tier wine label.  I would like it to be in a light, natural color with silver or gold.  I would like it to look rich and expensive, mostly monochromatic, elegantly simple.  It will need to stand up next to wine labels that are black and charcoal colored and look like the more expensive wine of the 3.  I have attached a similar label that it will be grouped with and some instructions.
We are a winery in southeast Washington state with a reputation for fine wines and top notch terroir.  We want to present family, tradition and high value wine in the bottle.

```html
<!DOCTYPE html>
<html lang="en">
<head>
<meta charset="utf-8">
<title>Lone Willow Estate – Vault Reserve Cabernet Sauvignon Labels</title>
<link rel="stylesheet" href="https://fonts.googleapis.com/css2?family=Cinzel:wght@400&family=Alegreya:wght@400&family=Great+Vibes&family=Dancing+Script&family=Roboto+Condensed:wght@400;700&display=swap">
<style>
  :root {
    --page: #ffffff;
    --paper: #f9f8ee;
    --gold: #c98a45;
    --silver: #bdbdc2;
    --silver-dark: #8e8e94;
    --frame: #b9b9bd;
    --body-text: #77746e;
    --ink: #1f1f1f;
    --band-start: #b4b4b8;
    --band-end: #ececee;
  }
  * { box-sizing: border-box; margin: 0; padding: 0; }
  html, body { width: 1200px; height: 1000px; overflow: hidden; background: var(--page); }
  .canvas { position: relative; width: 1200px; height: 1000px; }

  /* Front label */
  .front-label {
    position: absolute; left: 50px; top: 96px; width: 484px; height: 808px;
    background: var(--paper); text-align: center;
  }
  .front-label .frame {
    position: absolute; left: 17px; top: 16px; right: 17px; height: 713px;
    border: 2px solid var(--frame);
  }
  .front-label .line { position: absolute; left: 0; right: 0; }
  .brand-title {
    font-family: "Cinzel", serif; color: var(--gold); font-weight: 400;
    font-size: 58px; line-height: 1;
  }
  .front-label .title-1 { top: 100px; }
  .front-label .title-2 { top: 172px; }
  .estate-vineyard {
    top: 253px; font-family: "Alegreya", serif; color: var(--gold);
    font-size: 20px; letter-spacing: 2px;
  }
  .tier-script {
    top: 300px; font-family: "Great Vibes", cursive; color: var(--silver);
    font-size: 64px; line-height: 1;
  }
  .estate-mark {
    top: 440px; display: flex; justify-content: center; align-items: center; gap: 12px;
    font-family: "Cinzel", serif; color: var(--silver-dark); font-size: 22px; letter-spacing: 3px;
  }
  .estate-mark .mark-square { width: 18px; height: 18px; background: var(--silver-dark); }
  .varietal {
    top: 566px; font-family: "Alegreya", serif; color: var(--gold);
    font-size: 30px; letter-spacing: 3px;
  }
  .appellation { top: 645px; font-family: "Alegreya", serif; color: var(--gold); font-size: 20px; letter-spacing: 2px; }
  .vintage { top: 673px; font-family: "Alegreya", serif; color: var(--gold); font-size: 20px; letter-spacing: 1px; }
  .front-label .motto-band {
    position: absolute; left: 0; right: 0; bottom: 0; height: 65px;
    background: linear-gradient(90deg, var(--band-start), #d2d2d5 60%, var(--band-end));
    display: flex; align-items: center; justify-content: center;
    font-family: "Alegreya", serif; font-size: 14.5px; letter-spacing: 1.6px; color: var(--ink);
  }

  /* Back label */
  .back-label {
    position: absolute; left: 594px; top: 176px; width: 556px; height: 647px;
    background: var(--paper);
  }
  .back-label .brand-title {
    position: absolute; left: 0; right: 0; top: 36px; text-align: center; font-size: 41px;
  }
  .back-subtitle {
    position: absolute; left: 35px; right: 35px; top: 86px;
    display: flex; justify-content: space-between;
    font-family: "Alegreya", serif; color: var(--gold); font-size: 20px; letter-spacing: 2px;
  }
  .back-rule { position: absolute; left: 20px; width: 513px; top: 113px; height: 2px; background: var(--gold); opacity: .8; }
  .story {
    position: absolute; left: 35px; width: 484px; top: 120px;
    font-family: "Alegreya", serif; color: var(--body-text);
    font-size: 16.5px; line-height: 20px; text-align: justify; text-align-last: justify;
  }
  .signoff { position: absolute; left: 35px; font-family: "Alegreya", serif; color: var(--body-text); font-size: 16.5px; line-height: 21px; }
  .signoff .signature { font-family: "Dancing Script", cursive; color: #555; font-size: 15px; }
  .signoff-winemaker { top: 322px; }
  .signoff-proprietor { top: 381px; }
  .crest-area { position: absolute; left: 349px; top: 287px; width: 173px; height: 162px; }
  .warning {
    position: absolute; left: 11px; top: 468px; width: 264px;
    font-family: "Roboto Condensed", sans-serif; font-size: 13.5px; line-height: 18px; color: var(--ink);
  }
  .warning strong, .bottling strong { font-weight: 700; }
  .bottling {
    position: absolute; right: 14px; top: 468px; width: 290px; text-align: right;
    font-family: "Roboto Condensed", sans-serif; font-size: 13.5px; line-height: 18px; color: var(--ink);
  }
  .back-label .edge-band {
    position: absolute; left: 0; right: 0; bottom: 0; height: 15px;
    background: linear-gradient(90deg, var(--band-end), var(--band-start) 50%, var(--band-end));
  }
</style>
</head>
<body>
<main class="canvas">

  <section class="front-label" aria-label="Front label">
    <div class="frame"></div>
    <h1 class="line brand-title title-1">LONE WILLOW</h1>
    <div class="line brand-title title-2">ESTATE</div>
    <p class="line estate-vineyard">ESTATE VINEYARD</p>
    <p class="line tier-script">Vault Reserve</p>
    <div class="line estate-mark"><span class="mark-square"></span><span>LONE WILLOW ESTATE</span></div>
    <p class="line varietal">CABERNET SAUVIGNON</p>
    <p class="line appellation">HORSE HEAVEN HILLS</p>
    <p class="line vintage">2022</p>
    <div class="motto-band">FAMILY STEWARDS OF THE LAND FOR 5 GENERATIONS</div>
  </section>

  <section class="back-label" aria-label="Back label">
    <h2 class="brand-title">LONE WILLOW ESTATE</h2>
    <div class="back-subtitle"><span>VAULT RESERVE</span><span>CABERNET SAUVIGNON</span></div>
    <div class="back-rule"></div>
    <p class="story">Lone Willow Estate wines are exclusively sourced from our family's Estate Vineyard in the Horse Heaven Hills of Washington state. For five generations, we have cultivated this rugged and fertile land, embodying our deep-seated love and dedication. We believe that exceptional wine is the result of outstanding vineyards, limited production, and astute winemaking. With the utmost pride and joy, we present this exquisite Cabernet Sauvignon from our ranch to your table.</p>

    <p class="signoff signoff-winemaker">Cheers, <span class="signature">Marion Hale</span><br>Marion Hale, Winemaker</p>
    <p class="signoff signoff-proprietor">Cheers, <span class="signature">Dale Whitcomb</span><br>Dale Whitcomb, Farmer &amp; Proprietor</p>

    <svg class="crest-area" viewBox="0 0 173 162" role="img" aria-label="Family crest artwork">
      <defs>
        <radialGradient id="crestTone" cx="50%" cy="50%" r="60%">
          <stop offset="0%" stop-color="#cfcfd2"/>
          <stop offset="100%" stop-color="#f0f0ee"/>
        </radialGradient>
      </defs>
      <rect width="173" height="162" fill="url(#crestTone)"/>
    </svg>

    <p class="warning"><strong>GOVERNMENT WARNING:</strong> (1) ACCORDING TO THE SURGEON GENERAL, WOMEN SHOULD NOT DRINK ALCOHOLIC BEVERAGES DURING PREGNANCY BECAUSE OF THE RISK OF BIRTH DEFECTS. (2) CONSUMPTION OF ALCOHOLIC BEVERAGES IMPAIRS YOUR ABILITY TO DRIVE A CAR OR OPERATE MACHINERY, AND MAY CAUSE HEALTH PROBLEMS.</p>
    <p class="bottling"><strong>750 ML</strong> CONTAINS SULFITES<br>15% ALC. BY VOL.<br><strong>PRODUCED AND BOTTLED BY:</strong> WHITCOMB WINE ESTATES, LLC, KELLEN WA, USA</p>
    <div class="edge-band"></div>
  </section>

</main>
</body>
</html>
```